Dietary supplement, Clean and simple.

Hi,
I’d like to talk about the project,

About us:
We are a dietary supplement (Vitamins, Minerals, amino acids etc.) company.
The goal is to have about 25 products at the end of this year. However, for this goal to be achieved we need a good label design to make our products represent our company values.
I’ll be here every day supporting your questions, we are fully committed to making the highest/best quality/customer experience possible.

About the design and our values:
- Professional (We are in the industry of professionalism and expertise. I would love to show we are competent at this, Id. Like to have the labels looks like we have done our research.)
- Efficient (White spacing, good use of the space available.)
- Simple (Straight forward, in 5 seconds they have to know what the product they have is/how functions. We’re trying to simplify it for the consumer.
- No distractions (the only visually “distracting” factor can be the vector art.)

The guidelines:
The goal is to have a universal design, with one element that changes (Vector art). I’ll attach a file/multiple files I think can show some visuals on what I’m looking for, and what parts of the design I think are good/bad.

Label size: 69x155mm (Front is 77.5mm)

Design whatever you think fits our image. You’re the design expert, all I care about is that it fits our company standards/image.

Use this color/font.
Font: Sans Serif
Main company color is Mind green #237D62 (Use this color for something in the design.)

What I thought would be cool/might looks ugly, who knows:
1. The front of the label: Should have 1 vector art, preferably in the top right corner. (That looks good in multiple colors. The vector can have multiple areas to color, I would prefer 2 main colors in the vector art. The interchangeable colors are used for multiple kinds of products.)
2. Text/product information on the left. The text that will have to be displayed:
- Product name for instance “Magnesium + B6”
- Description for the product for instance “Magnesium with ginger taste”
- Company name or logo. (Add ® behind it. We are soon to be trademark registered.)
3. We need to show the "daily intake" amount on the front and also the amount in the complete bottle. For instance, “Daily intake 1 capsule, 60 capsules”.
• You don’t have to design the backside of the label. After I chose a design, I’d like to chat and give specific information on what areas need to be assigned where. (Too complex because of the law.)
Updates

Hi, Please make the deadline 31 days total. I want designers to have the time to design. And not be rushed to finish it.

I want to extend the deadline because i feel like a slightly more medical look would be interesting. Hope you can come up with something!!

Target Market(s)

Dietary supplement consumers

Industry/Entity Type

Dietary supplements

Font styles to use
Sans Serif

Colors

Designer to choose colors to be used in the design.

Requirements
Must have
• Trademark icon "®" has to be at the top right after the company logo(text of logo)/name.

```html
<!DOCTYPE html>
<html lang="en">
<head>
<meta charset="utf-8">
<title>Ardena Well – Magnesium + B6 Label</title>
<link href="https://fonts.googleapis.com/css2?family=Oswald:wght@400;500;600&display=swap" rel="stylesheet">
<style>
  :root {
    --backdrop: #b9bcbe;
    --label-green-deep: #a6d1ae;
    --label-green-light: #e6f0e8;
    --brand-green: #237d62;
    --accent-green: #2f9e46;
    --ink: #2b2b2b;
    --badge: #2a2a2a;
    --white: #ffffff;
  }
  * { margin: 0; padding: 0; box-sizing: border-box; }
  html, body {
    width: 1200px;
    height: 810px;
    overflow: hidden;
    background: var(--backdrop);
    font-family: "Oswald", sans-serif;
  }
  .canvas {
    position: relative;
    width: 1200px;
    height: 810px;
  }
  .label {
    position: absolute;
    left: 320px;
    top: 45px;
    width: 560px;
    height: 720px;
    background: linear-gradient(160deg, var(--label-green-deep) 0%, #c2e0c7 45%, var(--label-green-light) 100%);
    overflow: hidden;
  }
  .fruit-art {
    position: absolute;
    right: 0;
    top: 0;
    width: 410px;
    height: 250px;
    background: radial-gradient(ellipse at 55% 35%, #c8424e 0%, #d9735a 30%, #b8d39a 60%, rgba(184,211,154,0) 80%);
  }
  .brand {
    position: absolute;
    left: 18px;
    top: 296px;
    color: var(--brand-green);
  }
  .brand-name {
    font-weight: 600;
    font-size: 64px;
    line-height: 1;
    letter-spacing: 2px;
    text-transform: uppercase;
  }
  .brand-reg {
    position: absolute;
    right: -40px;
    top: -14px;
    font-weight: 600;
    font-size: 34px;
    line-height: 1;
  }
  .product-name {
    position: absolute;
    left: 15px;
    top: 448px;
    font-weight: 500;
    font-size: 66px;
    line-height: 1.1;
    color: var(--ink);
  }
  .divider {
    position: absolute;
    left: 15px;
    top: 540px;
    width: 362px;
    border-top: 3px dotted var(--accent-green);
  }
  .description {
    position: absolute;
    left: 15px;
    top: 562px;
    font-weight: 500;
    font-size: 25px;
    color: var(--ink);
  }
  .intake {
    position: absolute;
    left: 15px;
    top: 612px;
    font-weight: 400;
    font-size: 19px;
    color: var(--ink);
  }
  .category {
    position: absolute;
    left: 15px;
    top: 650px;
    font-weight: 500;
    font-size: 29px;
    color: var(--accent-green);
    text-transform: uppercase;
  }
  .count-badge {
    position: absolute;
    left: 413px;
    top: 584px;
    width: 114px;
    height: 114px;
    border-radius: 50%;
    background: var(--badge);
    color: var(--white);
    display: flex;
    flex-direction: column;
    align-items: center;
    justify-content: center;
    text-transform: uppercase;
    line-height: 1.1;
  }
  .count-number { font-size: 32px; font-weight: 600; }
  .count-unit { font-size: 18px; font-weight: 400; }
</style>
</head>
<body>
  <div class="canvas">
    <div class="label">
      <div class="fruit-art" role="img" aria-label="Illustration of assorted fruits and berries: pomegranate, strawberry, cherries, mango, grapes, banana and gooseberries"></div>

      <div class="brand">
        <span class="brand-name">Ardena Well</span>
        <span class="brand-reg">®</span>
      </div>

      <h1 class="product-name">Magnesium + B6</h1>
      <div class="divider"></div>
      <p class="description">Magnesium with ginger taste</p>
      <p class="intake">Daily Intake 1 Capsule</p>
      <p class="category">Dietary Supplement</p>

      <div class="count-badge">
        <span class="count-number">60</span>
        <span class="count-unit">Capsules</span>
      </div>
    </div>
  </div>
</body>
</html>
```